Stationery Design Project

We need a stationary design (business card, logo, letterhead) for a new company called "Brightwell Junctions".
We provide software and consulting services to improve business efficiency & increase team engagement.
We focus on workflow automation, business social networking software and collaboration and communication tools built on mobile platforms.
Updates

Target Market(s)

Business with multi-site,young, mobile workforces e.g Retailers, Hospitality

Industry/Entity Type

Communication

Requirements
Must have
• Letterhead to include;
Business Address: 17 Kelvane St, Marrowby Flats, NSW 2187
ABN : 58 417 620 384

```html
<!DOCTYPE html>
<html lang="en">
<head>
<meta charset="utf-8">
<title>Brightwell Junctions – Stationery</title>
<link href="https://fonts.googleapis.com/css2?family=Michroma&family=Roboto:ital,wght@0,400;0,700;1,700&display=swap" rel="stylesheet">
<style>
  :root {
    --backdrop: #4a4a4a;
    --teal: #17a398;
    --teal-deep: #00695f;
    --paper: #ffffff;
    --card-dark: #2b2624;
    --card-glow: #463f3b;
    --ink: #222222;
    --card-text: #d8d4d0;
  }
  * { margin: 0; padding: 0; box-sizing: border-box; }
  html, body { width: 1200px; height: 1200px; overflow: hidden; }
  body {
    position: relative;
    background: var(--backdrop);
    font-family: "Roboto", Arial, sans-serif;
  }
  .wordmark {
    font-family: "Michroma", "Arial", sans-serif;
    font-weight: 400;
    color: var(--teal);
    text-transform: uppercase;
    line-height: 1.1;
    display: flex;
    align-items: center;
    gap: 0.5em;
    white-space: nowrap;
  }
  .wordmark .mark-dot {
    width: 1.6em; height: 1.6em;
    border-radius: 50%;
    background: currentColor;
    flex: none;
  }

  /* Letterhead */
  .letterhead {
    position: absolute;
    left: 55px; top: 97px;
    width: 568px; height: 799px;
    background: var(--paper);
    overflow: hidden;
  }
  .letterhead .accent { position: absolute; background: var(--teal); width: 15px; height: 87px; }
  .letterhead .accent.top-left { left: 0; top: 0; }
  .letterhead .accent.bottom-left { left: 0; bottom: 0; }
  .letterhead .accent.bottom-right { right: 0; bottom: 0; }
  .letterhead .wordmark { position: absolute; left: 44px; top: 36px; font-size: 13px; }
  .letterhead-footer {
    position: absolute; left: 0; top: 744px; width: 100%;
    font-size: 8.5px; line-height: 1.5; color: var(--ink);
  }
  .letterhead-footer .col { position: absolute; top: 0; white-space: nowrap; }
  .letterhead-footer .col.company { left: 73px; }
  .letterhead-footer .col.address { left: 212px; }
  .letterhead-footer .col.contact { left: 358px; }

  /* Business cards */
  .card {
    position: absolute;
    left: 713px; width: 438px;
    background: radial-gradient(ellipse at 55% 45%, var(--card-glow), var(--card-dark) 75%);
    overflow: hidden;
  }
  .card-front { top: 93px; height: 251px; }
  .card-front .bar { position: absolute; top: 16px; width: 8px; height: 218px; background: var(--teal); }
  .card-front .bar.left { left: 3px; }
  .card-front .bar.right { right: 3px; }
  .card-front .wordmark { position: absolute; left: 0; right: 0; top: 103px; justify-content: center; font-size: 18px; }

  .card-back { top: 363px; height: 249px; }
  .card-back .bar { position: absolute; left: 3px; top: 17px; width: 5px; height: 114px; background: var(--teal); }
  .card-back .wordmark { position: absolute; left: 28px; top: 42px; font-size: 12px; }
  .card-back .rule { position: absolute; left: 5px; top: 106px; width: 200px; height: 2px; background: var(--teal); }
  .card-back .person-name {
    position: absolute; left: 28px; top: 105px;
    font-weight: 700; font-style: italic; font-size: 20px; color: #ffffff; letter-spacing: 1px;
  }
  .card-back .role-band {
    position: absolute; left: 5px; top: 130px; width: 140px; height: 17px;
    background: var(--teal);
    clip-path: polygon(0 0, 92% 0, 100% 50%, 92% 100%, 0 100%);
  }
  .card-back .role {
    position: absolute; left: 150px; top: 132px;
    font-size: 11px; color: var(--teal);
  }
  .contact-list {
    position: absolute; left: 24px; top: 165px;
    list-style: none; font-size: 11px; color: var(--card-text);
  }
  .contact-list li { display: flex; align-items: center; gap: 8px; height: 16.5px; white-space: nowrap; }
  .contact-list svg { width: 11px; height: 11px; flex: none; }

  /* Logo presentation bands */
  .logo-band {
    position: absolute; top: 993px; height: 207px;
    display: flex; align-items: center; justify-content: center;
  }
  .logo-band.light { left: 0; width: 595px; background: var(--paper); }
  .logo-band.dark { left: 595px; width: 605px; background: var(--teal-deep); }
  .logo-band .wordmark { font-size: 30px; }
  .logo-band.dark .wordmark { color: #ffffff; }
</style>
</head>
<body>

  <section class="letterhead" aria-label="Letterhead">
    <span class="accent top-left"></span>
    <span class="accent bottom-left"></span>
    <span class="accent bottom-right"></span>
    <div class="wordmark"><span class="mark-dot"></span><span>Brightwell<br>Junctions</span></div>
    <footer class="letterhead-footer">
      <div class="col company">BRIGHTWELL JUNCTIONS<br>ABN : 58 417 620 384</div>
      <div class="col address">17 Kelvane St, Marrowby Flats,<br>NSW 2187</div>
      <div class="col contact">telephone: + 61 2 9104 5726<br>web: www.brightwelljunctions.com</div>
    </footer>
  </section>

  <section class="card card-front" aria-label="Business card front">
    <span class="bar left"></span>
    <span class="bar right"></span>
    <div class="wordmark"><span class="mark-dot"></span><span>Brightwell<br>Junctions</span></div>
  </section>

  <section class="card card-back" aria-label="Business card back">
    <span class="bar"></span>
    <div class="wordmark"><span class="mark-dot"></span><span>Brightwell<br>Junctions</span></div>
    <span class="rule"></span>
    <h2 class="person-name">DAN HARKER</h2>
    <span class="role-band"></span>
    <span class="role">Director</span>
    <ul class="contact-list">
      <li><svg viewBox="0 0 12 12"><rect x="3" y="0.5" width="6" height="11" rx="1" fill="none" stroke="#d8d4d0"/><rect x="5" y="9" width="2" height="1" fill="#d8d4d0"/></svg>+ 61 455 203 917</li>
      <li><svg viewBox="0 0 12 12"><path d="M3 1 L5 3 L4 5 Q5 7 7 8 L9 7 L11 9 L9 11 Q2 9 1 3 Z" fill="#d8d4d0"/></svg>+ 61 2 9104 5726</li>
      <li><svg viewBox="0 0 12 12"><rect x="0.5" y="2.5" width="11" height="7" fill="none" stroke="#d8d4d0"/><path d="M0.5 2.5 L6 7 L11.5 2.5" fill="none" stroke="#d8d4d0"/></svg>dan.harker@brightwelljunctions.com</li>
      <li><svg viewBox="0 0 12 12"><circle cx="6" cy="6" r="5.3" fill="none" stroke="#d8d4d0"/><ellipse cx="6" cy="6" rx="2.3" ry="5.3" fill="none" stroke="#d8d4d0"/><line x1="0.7" y1="6" x2="11.3" y2="6" stroke="#d8d4d0"/></svg>brightwelljunctions.com</li>
    </ul>
  </section>

  <section class="logo-band light" aria-label="Logo on white">
    <div class="wordmark"><span class="mark-dot"></span><span>Brightwell<br>Junctions</span></div>
  </section>
  <section class="logo-band dark" aria-label="Logo reversed on teal">
    <div class="wordmark"><span class="mark-dot"></span><span>Brightwell<br>Junctions</span></div>
  </section>

</body>
</html>
```